Banner for home page on event planning site

We are revamping the home page www.harborlanecelebrations.com and would like to add a banner to the center of it to guide potential clients to one of 3 areas of the site:

Weddings, Corporate Events, Parties and More

I'm uploading an attachment that shows where the banner will be placed. It needs to have those 3 distinct sections, and match the existing colors/branding of the site. The fonts used for the logo are Lucida Bright and Callie Hand. Both are available for free.

Please use lorem ipsum under each section, I'll fill that in later. It should just be highly designed, beautiful, and easy to understand that clicking these will take you to the different areas of the site.
Updates

Hi designers,
Here are some problems we are having with the designs that have been submitted.
1) 3 stock images as squares... when you do this and then put it into the existing website, it gets lost among the other boxes. We need this to be where the eye goes immediately when you land on the site.
2) Not enough of a frame or white space... we think you need some white space to make this stand out as different from the surrounding area.
3) No clearly defined areas. It needs to be easy for people to figure out... Weddings, click here. Parties, click here. Corporate events, click here.

Industry/Entity Type

Event Planning

Requirements
Should not have
• Nothing with orchids, her competitor uses them and they are common in the event planning industry. We want to stay away from them.

```html
<!DOCTYPE html>
<html lang="en">
<head>
<meta charset="utf-8">
<title>Harbor Lane Celebrations — Event Categories Banner</title>
<link rel="stylesheet" href="https://fonts.googleapis.com/css2?family=Cinzel:wght@500&display=swap">
<style>
  :root {
    --wood-dark: #3d2a18;
    --wood-mid: #5a4029;
    --wood-light: #6b4d31;
    --sky-top: #c9cdf6;
    --sky-mid: #dfe3fb;
    --sky-glow: #f4f6ff;
    --floor-top: #f7f7f9;
    --floor-bottom: #e6e6ea;
    --ring: #b64ea0;
    --ribbon-light: #cf63b3;
    --ribbon-main: #b6449a;
    --ribbon-dark: #8c2f75;
    --ribbon-fold: #6e2259;
    --label: #ffffff;
  }
  * { margin: 0; padding: 0; box-sizing: border-box; }
  html, body {
    width: 1200px;
    height: 346px;
    overflow: hidden;
  }
  body {
    position: relative;
    background: linear-gradient(90deg, var(--wood-dark), var(--wood-mid) 30%, var(--wood-light) 55%, var(--wood-mid) 80%, var(--wood-dark));
    font-family: "Cinzel", "Times New Roman", serif;
  }
  .banner {
    position: absolute;
    left: 42px;
    top: 43px;
    width: 1116px;
    height: 261px;
    overflow: hidden;
    box-shadow: 0 2px 8px rgba(0, 0, 0, 0.55);
    background:
      radial-gradient(ellipse 420px 200px at 33% 10%, var(--sky-glow), transparent 70%),
      radial-gradient(ellipse 380px 180px at 82% 30%, rgba(255,255,255,0.8), transparent 70%),
      linear-gradient(180deg, var(--sky-top), var(--sky-mid) 80%);
  }
  .banner__floor {
    position: absolute;
    left: 0;
    right: 0;
    top: 203px;
    bottom: 0;
    background: linear-gradient(180deg, var(--floor-top), var(--floor-bottom));
  }
  .category {
    position: absolute;
    top: 0;
    width: 340px;
    height: 261px;
    text-decoration: none;
  }
  .category--corporate { left: 24px; }
  .category--weddings { left: 388px; }
  .category--parties { left: 753px; }
  .category__photo {
    position: absolute;
    left: 72px;
    top: 12px;
    width: 196px;
    height: 196px;
    border-radius: 50%;
    border: 5px solid var(--ring);
    box-shadow: 0 0 0 2px rgba(255,255,255,0.5), 0 3px 8px rgba(60, 20, 60, 0.35);
  }
  .category--corporate .category__photo {
    background: radial-gradient(circle at 45% 40%, #e9dcc0, #7a6a55 55%, #1e1e26 90%);
  }
  .category--weddings .category__photo {
    background: radial-gradient(circle at 50% 45%, #f2e3c9, #c9b27a 50%, #7d8a4a 80%, #2a2a2a);
  }
  .category--parties .category__photo {
    background: radial-gradient(circle at 50% 55%, #b98a4e, #7b4a26 55%, #3a1e14 90%);
  }
  .category__ribbon {
    position: absolute;
    left: 0;
    top: 188px;
    width: 340px;
    height: 60px;
  }
  .category__label {
    position: absolute;
    left: 0;
    right: 0;
    top: 199px;
    text-align: center;
    color: var(--label);
    font-size: 27px;
    font-weight: 500;
    letter-spacing: 0.5px;
    text-shadow: 0 1px 2px rgba(80, 10, 60, 0.6);
  }
  .category__reflection {
    position: absolute;
    left: 30px;
    top: 248px;
    width: 280px;
    height: 13px;
    background: linear-gradient(180deg, rgba(182, 68, 154, 0.18), transparent);
  }
</style>
</head>
<body>
  <svg width="0" height="0" style="position:absolute" aria-hidden="true">
    <defs>
      <linearGradient id="ribbon-face" x1="0" y1="0" x2="0" y2="1">
        <stop offset="0" stop-color="#cf63b3"/>
        <stop offset="0.55" stop-color="#b6449a"/>
        <stop offset="1" stop-color="#9a3582"/>
      </linearGradient>
      <linearGradient id="ribbon-tail" x1="0" y1="0" x2="0" y2="1">
        <stop offset="0" stop-color="#b6449a"/>
        <stop offset="1" stop-color="#8c2f75"/>
      </linearGradient>
      <symbol id="ribbon" viewBox="0 0 340 60">
        <path d="M8 0 H53 V46 H8 L22 23 Z" fill="url(#ribbon-tail)"/>
        <path d="M332 0 H287 V46 H332 L318 23 Z" fill="url(#ribbon-tail)"/>
        <path d="M44 46 L53 46 L53 56 Z" fill="#6e2259"/>
        <path d="M296 46 L287 46 L287 56 Z" fill="#6e2259"/>
        <path d="M44 8 Q170 2 296 8 V52 Q170 58 44 52 Z" fill="url(#ribbon-face)"/>
      </symbol>
    </defs>
  </svg>

  <main class="banner">
    <div class="banner__floor"></div>

    <a class="category category--corporate" href="#corporate-events">
      <div class="category__photo" role="img" aria-label="Photo of guests raising champagne glasses in a toast"></div>
      <svg class="category__ribbon" aria-hidden="true"><use href="#ribbon"/></svg>
      <span class="category__label">Corporate Events</span>
      <div class="category__reflection"></div>
    </a>

    <a class="category category--weddings" href="#weddings">
      <div class="category__photo" role="img" aria-label="Photo of a smiling bride and groom with a white bouquet"></div>
      <svg class="category__ribbon" aria-hidden="true"><use href="#ribbon"/></svg>
      <span class="category__label">Weddings</span>
      <div class="category__reflection"></div>
    </a>

    <a class="category category--parties" href="#parties">
      <div class="category__photo" role="img" aria-label="Photo of guests dancing at a lively party in a banquet hall"></div>
      <svg class="category__ribbon" aria-hidden="true"><use href="#ribbon"/></svg>
      <span class="category__label">Parties</span>
      <div class="category__reflection"></div>
    </a>
  </main>
</body>
</html>
```